Poster for a 100 y.o. Tennis Tournament

I would like a poster designed to promote our tennis tournament but I'd like to avoid some of the clichés like the shadow of a player serving. Just well styled text would be fine but some clever imagery would be a bonus.
Highlighting the fact our tournament has been running for over 100 years would be nice so a retro design would work. But that doesn't mean a modern design, for example a minimalist approach utilising the lines of a tennis court, wouldn't work.
Updates

Our tennis committee is now in the process of short listing and will provide an update within 48 hours.

Industry/Entity Type

Court

Requirements
Must have
• The poster must contain the following text at a minimum:
"Marbury Tennis Tournament"/"Since 1908"
"9 March - 11 March, 2013" or "9-11 March, 2013", etc
"www.marburytennis.com.au"

The poster must be reproducible in colour and black & white, or at least have an alternate for black & white.

The poster must be usable in both A3 and A4 sizes.
Nice to have
• The poster should contain the following text:
"Championship"
"Handicap"
"Seniors"
"Juniors"
Each above may be optionally succeeded by "Singles & Doubles", e.g. "Championship Singles & Doubles". It would actually be clearer if this additional text was used but would be repetitive, so alternate text "Singles & Doubles in all categories" might also be used. Alternatives for variety (with the first word the focus): "Championship Singles & Doubles", "Handicap Singles & Doubles", "Seniors 35+ & 50+", "Juniors 18&U, 14&U"

Ideally the poster will provision room for four to eight sponsors logos, preferably at the bottom, but failure to do this is not a show stopper.

The following text may also be used:
"Entries close February 24"
"Tollard Plate Weekend"

Attached is a photo of one of the old trophies. Utilisation of the curved style of the "Marbury Tennis Tournament" text would fit in with the history if the tournament.

The ability to reuse elements of the poster in a single page website used to promote the tournament would be an advantage (as it will provide consistency).

If you could have an image of a tennis ball that conveys the same energy as the clock/tyre image in the attached "Under the Glass Moon" poster, that would be cool. Or using split imagery of a wooden racquet and a modern racquet, but with some energy, would also be good. These are just ideas though and by no means essential.

I've also attached a photo of a t-shirt with a poster layout I thought looked good.

Some additional text that can be used:
"Brand new courts"
"Brindle Park, Oakhurst Tce, Marbury"
"Phone 0427 318 642"
"Prizes and Trophies"

```html
<!DOCTYPE html>
<html lang="en">
<head>
<meta charset="utf-8">
<title>Marbury Tennis Tournament — 9th to 11th March, 2013</title>
<link rel="stylesheet" href="https://fonts.googleapis.com/css2?family=Bebas+Neue&family=Graduate&family=Alfa+Slab+One&display=swap">
<style>
  :root {
    --paper-light: #f6eee6;
    --paper-warm: #eedfd6;
    --paper-cool: #e6ddea;
    --ink: #262323;
    --sticker-blue: #86a6cb;
    --sticker-red: #cf5f70;
    --sticker-text: #f3ece8;
  }
  * { margin: 0; padding: 0; box-sizing: border-box; }
  html, body { width: 849px; height: 1200px; overflow: hidden; }
  body { background: var(--paper-light); }

  .poster {
    position: relative;
    width: 849px;
    height: 1200px;
    overflow: hidden;
    color: var(--ink);
    background:
      radial-gradient(ellipse at 20% 15%, rgba(255,255,255,0.6), transparent 55%),
      radial-gradient(ellipse at 85% 60%, rgba(214,196,226,0.45), transparent 60%),
      radial-gradient(ellipse at 10% 90%, rgba(236,205,200,0.5), transparent 55%),
      linear-gradient(170deg, var(--paper-light), var(--paper-warm) 45%, var(--paper-cool));
  }

  .line {
    position: absolute;
    left: 0;
    width: 100%;
    text-align: center;
    line-height: 1;
    white-space: nowrap;
  }

  .event-dates  { top: 14px;  font-family: "Alfa Slab One", serif; font-size: 40px; letter-spacing: 1px; }
  .headline     { font-family: "Bebas Neue", sans-serif; font-size: 150px; letter-spacing: 3px; }
  .headline--top    { top: 86px; }
  .headline--bottom { top: 222px; letter-spacing: 6px; }
  .since        { top: 364px; font-family: "Alfa Slab One", serif; font-size: 32px; letter-spacing: 1px; }

  .category     { font-family: "Graduate", serif; font-size: 76px; letter-spacing: 1px; }
  .category-note{ font-family: "Graduate", serif; font-size: 36px; letter-spacing: 1px; }
  .championship      { top: 440px; }
  .championship-note { top: 515px; }
  .handicap          { top: 590px; }
  .handicap-note     { top: 664px; font-size: 33px; }
  .seniors           { top: 728px; }
  .seniors-note      { top: 800px; font-size: 30px; }
  .juniors           { top: 865px; }
  .juniors-note      { top: 940px; font-size: 29px; }

  .entries-close { top: 1008px; font-family: "Bebas Neue", sans-serif; font-size: 62px; letter-spacing: 1px; }
  .website       { top: 1064px; font-family: "Bebas Neue", sans-serif; font-size: 44px; letter-spacing: 1px; }

  .sticker {
    position: absolute;
    width: 190px;
    height: 190px;
  }
  .sticker svg { position: absolute; inset: 0; }
  .sticker-text {
    position: absolute;
    inset: 0;
    display: flex;
    align-items: center;
    justify-content: center;
    text-align: center;
    font-family: "Bebas Neue", sans-serif;
    font-size: 40px;
    line-height: 0.95;
    color: var(--sticker-text);
  }
  .sticker--courts { left: -2px; top: 752px; transform: rotate(-20deg); }
  .sticker--courts .fill { fill: var(--sticker-blue); stroke: var(--sticker-blue); }
  .sticker--prizes { left: 660px; top: 686px; transform: rotate(22deg); }
  .sticker--prizes .fill { fill: var(--sticker-red); stroke: var(--sticker-red); }
</style>
</head>
<body>
<main class="poster">
  <p class="line event-dates">9TH TO 11TH MARCH, 2013</p>
  <h1>
    <span class="line headline headline--top">MARBURY TENNIS</span>
    <span class="line headline headline--bottom">TOURNAMENT</span>
  </h1>
  <p class="line since">SINCE 1908</p>

  <h2 class="line category championship">CHAMPIONSHIP</h2>
  <p class="line category-note championship-note">SINGLES AND DOUBLES</p>
  <h2 class="line category handicap">HANDICAP</h2>
  <p class="line category-note handicap-note">SINGLES AND DOUBLES</p>
  <h2 class="line category seniors">SENIORS</h2>
  <p class="line category-note seniors-note">35+ AND 50+</p>
  <h2 class="line category juniors">JUNIORS</h2>
  <p class="line category-note juniors-note">18&amp;U, 14&amp;U, GREEN BALL</p>

  <p class="line entries-close">ENTRIES CLOSE FEBRUARY 24</p>
  <p class="line website">WWW.MARBURYTENNIS.COM.AU</p>

  <div class="sticker sticker--courts">
    <svg viewBox="0 0 190 190" aria-hidden="true">
      <circle class="fill" cx="95" cy="95" r="82" stroke-width="12" stroke-dasharray="7 5"/>
    </svg>
    <p class="sticker-text">BRAND<br>NEW<br>COURTS!</p>
  </div>

  <div class="sticker sticker--prizes">
    <svg viewBox="0 0 190 190" aria-hidden="true">
      <circle class="fill" cx="95" cy="95" r="82" stroke-width="12" stroke-dasharray="7 5"/>
    </svg>
    <p class="sticker-text">PRIZES<br>AND<br>TROPHIES!</p>
  </div>
</main>
</body>
</html>
```